Pike Hauling Business Card Design Project

We need a new company business card. We provide professional timber harvesting (logging) and forest management services. I'm open to any creative design. Most company caps and shirts are navy blue and Light grey. Logo does not necessarily have to contain those colors. Logo containing picture of logging equipment, log truck, trees, or logs are acceptable. Be creative. Final logo should communicate our company's pride and professionalism in the Pike Hauling.
Updates

Target Market(s)

Timber owners, sawmills, and forestry professionals

Industry/Entity Type

Business

Requirements
Must have
• Must have Contact Info.
Phone: 936-402-5187
address: PO Box 8412
New Waverly, Tx 77358
www.rbpikehauling.example
rbpikehauling@mailbox.example
Owner: Ross Pike

Or design must leave room for this info.

```html
<!DOCTYPE html>
<html lang="en">
<head>
<meta charset="utf-8">
<title>Pike Hauling – Business Card</title>
<link rel="stylesheet" href="https://fonts.googleapis.com/css2?family=Arimo:wght@400;700&display=swap">
<style>
  :root {
    --backdrop: #1b1b1c;
    --card-top: #1d2225;
    --card-bottom: #121517;
    --brand-green: #8cd43a;
    --brand-gold: #a8802c;
    --text-grey: #9ea4a8;
    --muted-grey: #7d8387;
  }
  * { margin: 0; padding: 0; box-sizing: border-box; }
  html, body {
    width: 1200px; height: 900px; overflow: hidden;
    background: var(--backdrop);
    font-family: "Arimo", Helvetica, Arial, sans-serif;
  }
  .canvas {
    position: relative; width: 1200px; height: 900px;
    display: flex; flex-direction: column; align-items: center; justify-content: center; gap: 50px;
  }
  .card {
    position: relative; width: 560px; height: 320px;
    background: linear-gradient(160deg, var(--card-top), var(--card-bottom));
    box-shadow: 0 14px 30px rgba(0,0,0,.55);
  }
  .brand-mark {
    display: block; background: var(--brand-green);
  }
  .brand-name {
    color: var(--brand-gold); font-weight: 700; text-transform: uppercase;
    letter-spacing: 1px; line-height: 1;
  }

  /* back side */
  .card-back .brand {
    position: absolute; left: 70px; top: 118px;
    display: flex; align-items: center; gap: 20px;
  }
  .card-back .brand-mark { width: 84px; height: 74px; }
  .card-back .brand-name { font-size: 40px; }
  .card-back .address {
    position: absolute; right: 34px; bottom: 26px;
    font-size: 11px; color: var(--muted-grey); letter-spacing: .3px;
  }

  /* front side */
  .card-front .owner {
    position: absolute; right: 40px; top: 36px; text-align: left;
  }
  .owner-name { font-size: 36px; color: var(--brand-green); font-weight: 400; line-height: 1.05; }
  .owner-title { font-size: 16px; color: var(--muted-grey); margin-left: 42px; }
  .card-front .brand {
    position: absolute; left: 52px; top: 118px; width: 210px;
    display: flex; flex-direction: column; align-items: center; gap: 14px;
  }
  .card-front .brand-mark { width: 84px; height: 74px; }
  .card-front .brand-name { font-size: 31px; }
  .contacts {
    position: absolute; left: 318px; top: 160px; list-style: none;
    display: flex; flex-direction: column; gap: 15px;
  }
  .contact { display: flex; align-items: center; gap: 14px; font-size: 14px; color: var(--text-grey); }
  .contact svg { width: 20px; height: 20px; flex: none; fill: none; stroke: var(--brand-green); stroke-width: 1.8; }
  .contact svg .solid { fill: var(--brand-green); stroke: none; }
</style>
</head>
<body>
<main class="canvas">
  <section class="card card-back" aria-label="Card back">
    <div class="brand">
      <span class="brand-mark"></span>
      <span class="brand-name">Pike Hauling</span>
    </div>
    <p class="address">PO Box 8412, New Waverly, TX 77358 | USA</p>
  </section>

  <section class="card card-front" aria-label="Card front">
    <div class="owner">
      <p class="owner-name">Ross Pike</p>
      <p class="owner-title">Owner &amp; Proprietor</p>
    </div>
    <div class="brand">
      <span class="brand-mark"></span>
      <span class="brand-name">Pike Hauling</span>
    </div>
    <ul class="contacts">
      <li class="contact">
        <svg viewBox="0 0 24 24"><path class="solid" d="M6.6 10.8a15 15 0 0 0 6.6 6.6l2.2-2.2c.3-.3.7-.4 1-.2 1.1.4 2.3.6 3.6.6.6 0 1 .4 1 1V20c0 .6-.4 1-1 1A17 17 0 0 1 3 4c0-.6.4-1 1-1h3.5c.6 0 1 .4 1 1 0 1.3.2 2.5.6 3.6.1.3 0 .7-.2 1z"/></svg>
        <span>936-402-5187</span>
      </li>
      <li class="contact">
        <svg viewBox="0 0 24 24"><rect x="7" y="2.5" width="10" height="19" rx="1.5"/><line x1="7" y1="17" x2="17" y2="17"/><rect x="9" y="5" width="6" height="9"/></svg>
        <span>936-402-5187</span>
      </li>
      <li class="contact">
        <svg viewBox="0 0 24 24"><rect class="solid" x="2" y="5" width="20" height="14" rx="1"/><path d="M2.5 5.5 12 13l9.5-7.5" stroke="#15191b"/></svg>
        <span>rbpikehauling@mailbox.example</span>
      </li>
      <li class="contact">
        <svg viewBox="0 0 24 24"><circle cx="12" cy="12" r="9.5"/><ellipse cx="12" cy="12" rx="4.2" ry="9.5"/><line x1="2.5" y1="12" x2="21.5" y2="12"/><path d="M4.5 7h15M4.5 17h15"/></svg>
        <span>www.rbpikehauling.example</span>
      </li>
    </ul>
  </section>
</main>
</body>
</html>
```